I need a fresh looking, exciting and loaded design for Full service Restaurant

We need a web design for our restaurant, which offers full service Pakistani and Indian food in PA, USA. Design should be elegant, simplified so customers can navigate easily and order food online for catering as well as delivery. We need loads of pictures and room to grow. I already have a web address via vexlorin.com. It should include SSL and e-commerce for ordering food.
Be original and be creative and make it a fun site :)

Industry/Entity Type

Restaurant

```html
<!DOCTYPE html>
<html lang="en">
<head>
<meta charset="utf-8">
<title>Saffron Hollow — Fine Pak-Indian Cuisine</title>
<link href="https://fonts.googleapis.com/css2?family=Raleway:wght@400;500;600;700&display=swap" rel="stylesheet">
<style>
:root{
  --red:#d71920;
  --ink:#1b1b1b;
  --muted:#6b6b6b;
  --line:#e2e2e2;
  --dark:#0d0d0d;
  --white:#fff;
  --green:#3c8a2e;
}
*{box-sizing:border-box;margin:0;padding:0}
html,body{width:693px;height:1200px;overflow:hidden;background:#fff}
body{font-family:'Raleway',sans-serif;color:var(--ink);position:relative}
.abs{position:absolute}

/* header */
.site-header{left:0;top:0;width:693px;height:42px;background:#fff}
.brand{left:120px;top:8px;display:flex;align-items:center;gap:4px}
.brand-mark{width:14px;height:14px;border-radius:50%;background:var(--red)}
.brand-name{font-size:13px;font-weight:700;color:var(--red);line-height:1}
.brand-tag{left:138px;top:24px;font-size:5px;color:var(--muted)}
.topbar{left:274px;top:6px;display:flex;align-items:center;font-size:5px;color:#555;height:10px}
.topbar span{padding:0 9px;border-left:1px solid var(--line)}
.topbar span:first-child{border:0;padding-left:0;display:flex;align-items:center;gap:3px}
.social{display:flex;gap:3px}
.social i{display:block;width:9px;height:9px;border-radius:50%;background:#111}
.social i.on{background:var(--red)}
.topbar .social{margin-left:10px}
.main-nav{left:274px;top:29px;display:flex;gap:15px;font-size:4.6px;font-weight:600;color:#444;letter-spacing:.2px}
.main-nav .active{color:var(--red)}

/* hero */
.hero{left:0;top:42px;width:693px;height:258px;background:radial-gradient(ellipse at 70% 40%,#3c3530 0%,#2a241f 45%,#1c1814 100%)}
.hero-photo{position:absolute;inset:0;background:
  radial-gradient(circle at 8% 80%,rgba(176,140,40,.55) 0 18%,transparent 30%),
  radial-gradient(ellipse at 68% 55%,rgba(220,220,220,.25) 0 14%,transparent 30%),
  linear-gradient(90deg,rgba(0,0,0,.15),rgba(0,0,0,0))}
.hero-title{left:120px;top:89px;font-size:19px;font-weight:600;color:#fff}
.hero-sub{left:120px;top:115px;width:210px;font-size:7px;line-height:10px;color:#eee}
.hero-btn{left:120px;top:144px;width:66px;height:21px;border:1px solid #fff;outline:1px solid rgba(255,255,255,.5);outline-offset:1px;color:#fff;font-size:5.3px;display:flex;align-items:center;justify-content:center}
.hero-arrow{width:19px;height:19px;border:1px solid #ddd;display:flex;align-items:center;justify-content:center}
.hero-arrow.left{left:81px;top:121px}
.hero-arrow.right{left:592px;top:121px;border-color:var(--red)}

.quick-links{left:0;top:280px;width:693px;display:flex;justify-content:center;gap:12px}
.quick{width:42px;height:42px;border-radius:50%;background:#111;border:2px solid #fff;color:#fff;font-size:4.6px;font-weight:700;display:flex;flex-direction:column;align-items:center;justify-content:flex-end;padding-bottom:7px;text-align:center;line-height:5.5px}
.quick svg{margin-bottom:2px}
.quick.on{background:var(--red)}

/* headings */
.sec-title{left:0;width:693px;text-align:center;font-size:9px;font-weight:600}
.sec-title em{font-style:normal;color:var(--red)}
.divider{left:0;width:693px;display:flex;justify-content:center;align-items:center;gap:0}
.divider b{display:block;width:30px;height:1px;background:#888}
.divider i{display:flex;width:12px;height:12px;border-radius:50%;background:#555;align-items:center;justify-content:center}
.sec-sub{left:0;width:693px;text-align:center;font-size:5px;color:#555;line-height:7px}

/* category row */
.cats{left:120px;top:395px;display:flex;gap:12px}
.cat{width:104px;height:41px;border:1px solid var(--line);outline:1px solid #f0f0f0;outline-offset:1px;display:flex;align-items:center;padding-left:12px;gap:10px;background:#fff}
.cat.on{background:var(--red);color:#fff;outline-color:var(--red)}
.cat h4{font-size:7.5px;font-weight:500;text-align:center}
.cat p{font-size:4.5px;color:var(--muted);text-align:center}
.cat.on p{color:#fff}
.cat .txt{flex:1;padding-right:12px}

/* offer band */
.offer-band{left:0;top:456px;width:693px;height:199px;background:linear-gradient(90deg,#2b2521,#4a4039 40%,#3b342f 70%,#1f1b18)}
.offer-band::after{content:"";position:absolute;inset:0;background:rgba(0,0,0,.45)}
.offer-cards{left:120px;top:514px;display:flex;gap:12px;z-index:2}
.offer{width:104px;height:120px;background:#fff;padding:4px;text-align:center}
.offer .ph{height:48px}
.offer h5{font-size:5.5px;font-weight:700;margin-top:6px}
.offer p{font-size:4.5px;color:#555;line-height:6.5px;margin:4px 6px 0}
.offer .more{display:inline-block;margin-top:6px;border:1px solid var(--line);font-size:4.5px;padding:3px 8px;color:#555}
.offer .more.on{background:var(--red);color:#fff;outline:1px solid var(--red);outline-offset:1px}

/* special menu */
.menu-cards{left:120px;top:722px;display:flex;gap:12px}
.dish{width:104px;height:142px;position:relative}
.dish .box{position:absolute;left:7px;right:7px;bottom:0;height:76px;background:#fff;text-align:center;padding-top:5px}
.tag{display:inline-block;font-size:4px;border:1px solid var(--line);padding:1px 5px;color:#555}
.tag.on{background:var(--red);color:#fff;border-color:var(--red)}
.dish h5{font-size:5.8px;font-weight:700;margin-top:5px}
.dish p{font-size:4.5px;color:#555;line-height:6.5px;margin:3px 5px 0}
.dish .price{font-size:6px;font-weight:700;margin-top:4px}
.dish .price.on{color:var(--red)}

/* booking */
.booking{left:120px;top:938px;width:452px;height:62px;border:1px solid var(--line);outline:1px solid #f2f2f2;outline-offset:2px}
.field{top:14px;height:16px;border:1px solid var(--line);display:flex;align-items:center;font-size:5.3px;color:#444}
.field .ico{width:16px;height:100%;border-right:1px solid var(--line);display:flex;align-items:center;justify-content:center;margin-right:8px}
.find-btn{left:348px;top:14px;width:64px;height:14px;background:var(--red);color:#fff;font-size:5px;display:flex;align-items:center;justify-content:center;outline:1px solid var(--red);outline-offset:1px}
.hours{left:0;top:43px;width:452px;text-align:center;font-size:5.3px;color:#444}

/* promo banner */
.promo{left:120px;top:1008px;width:452px;height:60px;background:var(--dark);border:2px solid #111;overflow:hidden}
.promo-logo{left:0;top:0;width:117px;height:56px;background:#fff;display:flex;align-items:center;justify-content:center;gap:4px}
.promo-photo{left:290px;top:0;width:160px;height:56px;background:linear-gradient(160deg,#1b2a6b,#4a2f8f 55%,#1a1a3a);clip-path:polygon(14% 0,100% 0,100% 100%,0 100%)}
.promo h3{left:127px;top:9px;font-size:12px;font-weight:600;color:#fff;letter-spacing:.5px}
.promo h4{left:127px;top:26px;font-size:9px;font-weight:400;color:#fff}
.promo p{left:127px;top:41px;font-size:5.5px;color:#fff}
.promo p b{color:var(--red);font-size:9px;font-weight:400}

/* footer */
.site-footer{left:0;top:1078px;width:693px;height:98px;background:var(--dark);color:#ddd}
.fcol{top:16px;width:104px}
.fcol h6{font-size:5.3px;font-weight:700;color:#fff;letter-spacing:.3px;margin-bottom:8px}
.fcol p,.fcol li{font-size:4.5px;line-height:8px;list-style:none}
.post{display:flex;gap:5px;margin-bottom:4px}
.post .thumb{width:20px;height:20px;background:linear-gradient(135deg,#b5742a,#5e3a15)}
.post p{line-height:6.5px}
.post .date{color:var(--red)}
.subscribe{display:flex;margin-top:8px}
.subscribe span{width:80px;height:13px;background:#fff;color:#333;font-size:4.5px;font-style:italic;display:flex;align-items:center;padding-left:6px}
.subscribe b{width:24px;height:13px;background:var(--red);color:#fff;font-size:5px;display:flex;align-items:center;justify-content:center;font-weight:500}
.footer-social i{width:10px;height:10px;background:#fff}
.footer-social i.on{background:var(--red)}
.copyright{left:0;top:1176px;width:693px;height:24px;background:#1c1c1c;font-size:4.5px;color:#aaa;padding:10px 0 0 120px}
</style>
</head>
<body>

<header class="site-header abs">
  <div class="brand abs"><span class="brand-mark"></span><span class="brand-name">Saffron Hollow</span></div>
  <div class="brand-tag abs">A Fine Pak-Indian Cuisine</div>
  <div class="topbar abs">
    <span><svg width="6" height="6" viewBox="0 0 10 10"><path d="M2 1l2 2-1 1.5c.6 1.2 1.5 2.1 2.5 2.5L7 6l2 2-1.5 1.5C4.5 9 1 5.5.5 2.5z" fill="#444"/></svg>555-01-482-730</span>
    <span>Toll Free : 5550-193-274</span>
    <span>News / About / Contact</span>
    <div class="social"><i></i><i class="on"></i><i></i><i></i><i></i></div>
  </div>
  <nav class="main-nav abs">
    <span class="active">HOME</span><span>ABOUT US</span><span>ORDER ONLINE</span><span>MENU ⌄</span><span>OFFER/EVENTS</span><span>BLOG</span><span>CONTACT US</span>
  </nav>
</header>

<section class="hero abs">
  <div class="hero-photo" role="img" aria-label="Table of lentil curry, dried red chillies and spice bowls with a smiling waiter holding a glass on a tray"></div>
  <h1 class="hero-title abs">Welcome to Saffron Hollow</h1>
  <p class="hero-sub abs">Serving classic Indian cuisine to the Greater New Orleans area since 1982.</p>
  <div class="hero-btn abs">View Our Menu</div>
  <div class="hero-arrow left abs"><svg width="6" height="8" viewBox="0 0 6 8"><path d="M5 0L1 4l4 4" stroke="#fff" fill="none"/></svg></div>
  <div class="hero-arrow right abs"><svg width="6" height="8" viewBox="0 0 6 8"><path d="M1 0l4 4-4 4" stroke="#fff" fill="none"/></svg></div>
</section>

<div class="quick-links abs">
  <div class="quick"><svg width="10" height="9" viewBox="0 0 10 9"><path d="M0 1h2l1.5 5h5L10 2.5H3" stroke="#fff" fill="none"/><circle cx="4" cy="8" r=".8" fill="#fff"/><circle cx="8" cy="8" r=".8" fill="#fff"/></svg>Order<br>Online</div>
  <div class="quick on"><svg width="10" height="9" viewBox="0 0 10 9"><path d="M5 0L0 4.5h1.5V9h2.5V6h2v3h2.5V4.5H10z" fill="#fff"/></svg>Saffron<br>Hollow</div>
  <div class="quick"><svg width="10" height="9" viewBox="0 0 10 9"><path d="M1 1l4 3 4-3v7H1z" stroke="#fff" fill="none"/></svg>Dish the<br>Week</div>
</div>

<h2 class="sec-title abs" style="top:340px">Welcome To <em>SAFFRON HOLLOW</em></h2>
<div class="divider abs" style="top:352px"><b></b><i><svg width="6" height="6" viewBox="0 0 6 6"><path d="M1 1l4 4M5 1L1 5" stroke="#fff"/></svg></i><b></b></div>
<p class="sec-sub abs" style="top:367px;padding:0 220px">Fresh spices, slow-cooked curries and warm naan served every day by a family that has cooked together for three generations in our busy kitchen.</p>

<div class="cats abs">
  <div class="cat"><svg width="18" height="12" viewBox="0 0 18 12"><path d="M1 7a8 6 0 0116 0zM1 9h16M3 11h12" stroke="var(--red)" fill="none"/></svg><div class="txt"><h4>Food</h4><p>Cake &amp; Cookies</p></div></div>
  <div class="cat on"><svg width="16" height="14" viewBox="0 0 16 14"><circle cx="5" cy="8" r="4" stroke="#fff" fill="none"/><circle cx="11" cy="8" r="4" stroke="#fff" fill="none"/><path d="M8 1v3" stroke="#fff"/></svg><div class="txt"><h4>Drink</h4><p>Coffee &amp; Beer</p></div></div>
  <div class="cat"><svg width="18" height="12" viewBox="0 0 18 12"><ellipse cx="9" cy="6" rx="8" ry="4" stroke="var(--red)" fill="none"/><ellipse cx="9" cy="5" rx="4" ry="2" stroke="var(--red)" fill="none"/></svg><div class="txt"><h4>Chef</h4><p>Break Fast</p></div></div>
  <div class="cat"><svg width="10" height="14" viewBox="0 0 10 14"><path d="M2 2h6l-1 11H3zM6 2l2-2" stroke="var(--red)" fill="none"/></svg><div class="txt"><h4>Cocktail</h4><p>Fruit &amp; Tea</p></div></div>
</div>

<section class="offer-band abs" role="img" aria-label="Buffet hall with guests and chafing dishes"></section>
<h2 class="sec-title abs" style="top:474px;color:#fff;z-index:2">What We Offer</h2>
<div class="divider abs" style="top:486px;z-index:2"><b></b><i style="background:#ddd"><svg width="6" height="6" viewBox="0 0 6 6"><path d="M1 1l4 4M5 1L1 5" stroke="#555"/></svg></i><b></b></div>
<div class="offer-cards abs">
  <div class="offer"><div class="ph" role="img" aria-label="Plate of spiced chickpeas with rice" style="background:linear-gradient(120deg,#a23b12,#d9a25a 60%,#eee)"></div><h5>Brack Fast</h5><p>Hearty plates made fresh each morning with care.</p><span class="more">Read More...</span></div>
  <div class="offer"><div class="ph" role="img" aria-label="Grilled fish lunch plate" style="background:linear-gradient(120deg,#8a5a2a,#e6d8c8 50%,#c9502a)"></div><h5>Lunch</h5><p>Quick midday meals full of bright homestyle flavour.</p><span class="more on">Read More...</span></div>
  <div class="offer"><div class="ph" role="img" aria-label="Dinner table with drinks and fried snacks" style="background:linear-gradient(120deg,#cfc6b8,#b87a3a 55%,#6a3a1a)"></div><h5>Dinner</h5><p>Candlelit evenings with rich curries and biryani.</p><span class="more">Read More...</span></div>
  <div class="offer"><div class="ph" role="img" aria-label="Banquet hall set for an event" style="background:linear-gradient(120deg,#5a2a10,#d9a030 50%,#3a1a08)"></div><h5>Others</h5><p>Catering, parties and private events for any size.</p><span class="more">Read More...</span></div>
</div>

<h2 class="sec-title abs" style="top:673px">Special Menu</h2>
<div class="divider abs" style="top:685px"><b></b><i><svg width="6" height="6" viewBox="0 0 6 6"><path d="M1 1l4 4M5 1L1 5" stroke="#fff"/></svg></i><b></b></div>
<p class="sec-sub abs" style="top:701px">Chef picks for this week</p>

<div class="menu-cards abs">
  <div class="dish" role="img" aria-label="Salad bowl with beetroot and greens" style="background:linear-gradient(160deg,#5a3420,#9a5a3a 50%,#3a2418)"><div class="box"><span class="tag">New</span><h5>Baked Shrimp</h5><p>Grilled with garlic, lemon and house masala spice.</p><div class="price">$68</div></div></div>
  <div class="dish" role="img" aria-label="Broiled fish with vegetables" style="background:linear-gradient(160deg,#3e5a64,#c9a25a 50%,#6a4a2a)"><div class="box"><span class="tag">New</span><h5>Broiled Fish</h5><p>Grilled with garlic, lemon and house masala spice.</p><div class="price">$86</div></div></div>
  <div class="dish" role="img" aria-label="Shrimp and vegetables on a tray" style="background:linear-gradient(160deg,#c9b9a5,#6a8a4a 50%,#8a3a2a)"><div class="box"><span class="tag on">New</span><h5>Baked Shrimp</h5><p>Grilled with garlic, lemon and house masala spice.</p><div class="price on">$66</div></div></div>
  <div class="dish" role="img" aria-label="Fruit smoothie in a blender with fresh fruit" style="background:linear-gradient(160deg,#6aa83a,#c9d24a 45%,#c94a5a)"><div class="box"><span class="tag">New</span><h5>Fruit &amp; Tea</h5><p>Grilled with garlic, lemon and house masala spice.</p><div class="price">$88</div></div></div>
</div>

<h2 class="sec-title abs" style="top:883px">Book a Table</h2>
<div class="divider abs" style="top:895px"><b></b><i><svg width="6" height="6" viewBox="0 0 6 6"><path d="M1 1l4 4M5 1L1 5" stroke="#fff"/></svg></i><b></b></div>
<p class="sec-sub abs" style="top:910px">Powered By TableLine</p>

<section class="booking abs">
  <div class="field abs" style="left:16px;width:88px"><span class="ico"><svg width="6" height="6" viewBox="0 0 6 6"><rect x=".5" y="1" width="5" height="4.5" stroke="#999" fill="none"/></svg></span>02/02/2016</div>
  <div class="field abs" style="left:118px;width:102px"><span class="ico"><svg width="6" height="7" viewBox="0 0 6 7"><circle cx="3" cy="4" r="2.5" stroke="#666" fill="none"/></svg></span>7:00 pm</div>
  <div class="field abs" style="left:233px;width:103px"><span class="ico"><svg width="6" height="6" viewBox="0 0 6 6"><circle cx="3" cy="2" r="1.5" fill="#666"/><path d="M0 6a3 2.5 0 016 0z" fill="#666"/></svg></span>1 Person<svg style="margin-left:auto;margin-right:6px" width="5" height="3" viewBox="0 0 5 3"><path d="M0 0l2.5 3L5 0" stroke="#999" fill="none"/></svg></div>
  <div class="find-btn abs">Find a Table</div>
  <p class="hours abs">Openning Hour is 7:00 am-11:00pm every day on week</p>
</section>

<section class="promo abs">
  <div class="promo-logo abs"><span class="brand-mark"></span><span class="brand-name" style="font-size:11px">Saffron Hollow</span></div>
  <div class="promo-photo abs" role="img" aria-label="City hotel lit purple at night"></div>
  <h3 class="abs">SAFFRON HOLLOW</h3>
  <h4 class="abs">Pineapple Perfect Price Best Rate</h4>
  <p class="abs">Guaranteed or <b>15%</b> Off Your Stay!</p>
</section>

<footer class="site-footer abs">
  <div class="fcol abs" style="left:120px"><h6>ADDRESS</h6><p style="line-height:7px">Our dining room sits on the corner of Main Street.</p><p style="margin-top:4px"><b style="color:#fff">Phone:</b> 555-318-2046-771</p><p><b style="color:#fff">Email:</b> hello@saffronhollow.test</p></div>
  <div class="fcol abs" style="left:236px"><h6>RECENT POST</h6>
    <div class="post"><span class="thumb"></span><p>Weekend biryani<br>night returns<br><span class="date">June 7, 2013</span></p></div>
    <div class="post"><span class="thumb"></span><p>Weekend biryani<br>night returns<br><span class="date">June 7, 2013</span></p></div>
  </div>
  <div class="fcol abs" style="left:352px"><h6>BROWSE BY CATEGORY</h6><ul><li>All Recipes</li><li>Appetizers</li><li>Breakfast &amp; Brunch</li><li>Main Dish</li><li>Desserts</li><li>Drinks</li></ul></div>
  <div class="fcol abs" style="left:468px;width:110px"><h6>GET SOCIAL</h6><div class="social footer-social"><i></i><i class="on"></i><i></i><i></i><i></i></div><p style="margin-top:5px">Subscribe To our News latter Now!!</p><div class="subscribe"><span>Enter Your Email Address</span><b>SEND</b></div></div>
</footer>
<div class="copyright abs">Copyright © 2016 All Right Reserved.</div>

</body>
</html>
```